Sketch Harbor Business Card

I have attached several examples of business cards that I have seen online that I liked. We will be incorporating Spot UV coating and raised ink on the cards. Optionally we may use embossing with color. The business card will be used for 3d printing services. We are hoping to see some different color options of cards (i.e. black card, white card, etc.). We look forward to your ideas.

Industry/Entity Type

Printing

Requirements
Must have
• Dorian Makk
Founder and CEO
+1.555.010.2231 cell
+1.555.010.4786 office
+1.555.010.4786 fax
Dorian.Makk@3dKestrelo.com
www.3dKestrelo.com
Nice to have
• I would be nice to see some 3d background designs to add some depth to the designs of the cards since it is a 3d design company. There are examples of this in the files I have attached.

```html
<!DOCTYPE html>
<html lang="en">
<head>
<meta charset="utf-8">
<title>Sketch Harbor Business Card</title>
<link rel="stylesheet" href="https://fonts.googleapis.com/css2?family=PT+Sans+Narrow&display=swap">
<style>
  :root {
    --page: #ffffff;
    --band-blue: #0a84f0;
    --band-orange: #f28c00;
    --card-dark: #1d1d1d;
    --card-mid: #2a2a2a;
    --accent-yellow: #f4e600;
    --contact-text: #e8e8e8;
  }
  html, body {
    margin: 0;
    padding: 0;
    overflow: hidden;
    background: var(--page);
  }
  .canvas {
    position: relative;
    width: 1200px;
    height: 857px;
    overflow: hidden;
    background: var(--page);
  }
  .card {
    position: absolute;
    left: 180px;
    top: 265px;
    width: 720px;
    height: 367px;
    overflow: hidden;
    background: linear-gradient(180deg, var(--card-dark) 0%, var(--card-mid) 50%, var(--card-dark) 100%);
    font-family: "PT Sans Narrow", "Arial Narrow", sans-serif;
  }
  .band {
    position: absolute;
    left: 0;
    width: 100%;
    height: 38px;
    background: var(--band-blue);
  }
  .band--top { top: 0; }
  .band--bottom { bottom: 0; }
  .band__tab {
    position: absolute;
    width: 200px;
    height: 100%;
    background: var(--band-orange);
  }
  .band--top .band__tab {
    right: 0;
    border-bottom-left-radius: 22px;
  }
  .band--bottom .band__tab {
    left: 0;
    border-top-right-radius: 22px;
  }
  .holder {
    position: absolute;
    left: 25px;
    top: 52px;
    margin: 0;
    color: var(--accent-yellow);
    line-height: 1;
  }
  .holder__name {
    display: block;
    font-size: 40px;
    letter-spacing: 0.5px;
  }
  .holder__role {
    display: block;
    margin: 4px 0 0 63px;
    font-size: 29px;
  }
  .contact {
    position: absolute;
    right: 30px;
    bottom: 56px;
    margin: 0;
    padding: 0;
    list-style: none;
    text-align: right;
    color: var(--contact-text);
    font-size: 21px;
    line-height: 28px;
  }
  .contact__label {
    color: var(--accent-yellow);
  }
</style>
</head>
<body>
  <div class="canvas">
    <div class="card">
      <div class="band band--top"><div class="band__tab"></div></div>
      <p class="holder">
        <span class="holder__name">Dorian Makk</span>
        <span class="holder__role">Founder and CEO</span>
      </p>
      <ul class="contact">
        <li>+1.555.010.2231 <span class="contact__label">cell</span></li>
        <li>+1.555.010.4786 <span class="contact__label">office</span></li>
        <li>+1.555.010.4786 <span class="contact__label">fax</span></li>
        <li>Dorian.Makk@3dKestrelo.com</li>
        <li>www.3dKestrelo.com</li>
      </ul>
      <div class="band band--bottom"><div class="band__tab"></div></div>
    </div>
  </div>
</body>
</html>
```